Movie Poster for Crime/Thriller
We need a poster/DVD case which will grab your attention.

Target Market(s)

DVD Buyers and renters

Industry/Entity Type

Movie

Requirements
Must have
• Name of Film: The Quiet Ledger Affair
Pictures of the mask the gang uses.
The words "Greed, Betrayal, Murder, all components of"

```html
<!DOCTYPE html>
<html lang="en">
<head>
<meta charset="utf-8">
<title>The Quiet Ledger Affair — Poster</title>
<link rel="stylesheet" href="https://fonts.googleapis.com/css2?family=Anton&family=Oswald:wght@500&display=swap">
<style>
  :root {
    --ink-black: #050505;
    --charcoal: #1d1d1e;
    --blood-red: #b3191c;
    --title-red: #a8171b;
    --tag-grey: #b9b9b9;
    --mask-cream: #e2dfd2;
    --splatter: #a5121a;
  }
  html, body {
    margin: 0;
    padding: 0;
    overflow: hidden;
    background: var(--ink-black);
  }
  .poster {
    position: relative;
    width: 849px;
    height: 1200px;
    overflow: hidden;
    background: var(--charcoal);
  }
  .poster__spine-left {
    position: absolute;
    left: 0; top: 0;
    width: 116px; height: 100%;
    background: var(--ink-black);
  }
  .poster__spine-right {
    position: absolute;
    right: 0; top: 0;
    width: 27px; height: 100%;
    background: var(--blood-red);
  }
  .poster__art {
    position: absolute;
    inset: 0;
  }
  .title-text {
    font-family: "Anton", "Impact", sans-serif;
    fill: var(--title-red);
  }
  .tagline-text {
    font-family: "Oswald", "Arial Narrow", sans-serif;
    font-weight: 500;
    fill: var(--tag-grey);
  }
</style>
</head>
<body>
<main class="poster">
  <div class="poster__spine-left"></div>
  <div class="poster__spine-right"></div>

  <svg class="poster__art" width="849" height="1200" viewBox="0 0 849 1200">
    <defs>
      <radialGradient id="plain-mask-tone" cx="45%" cy="40%" r="65%">
        <stop offset="0" stop-color="#cfcfcc"/>
        <stop offset="1" stop-color="#9e9d9c"/>
      </radialGradient>
      <radialGradient id="clown-mask-tone" cx="50%" cy="45%" r="65%">
        <stop offset="0" stop-color="#e2dfd2"/>
        <stop offset="1" stop-color="#b9b4a6"/>
      </radialGradient>
    </defs>

    <g class="blood-splatter" role="img" aria-label="Splash of blood droplets">
      <ellipse cx="600" cy="285" rx="72" ry="55" fill="var(--splatter)"/>
      <circle cx="482" cy="290" r="17" fill="var(--splatter)"/>
      <circle cx="572" cy="378" r="22" fill="var(--splatter)"/>
    </g>

    <g class="gang-masks" role="img" aria-label="Two masks worn by the gang: a plain grey mask and a painted clown mask">
      <ellipse class="gang-masks__plain" cx="365" cy="645" rx="125" ry="212" fill="url(#plain-mask-tone)"/>
      <ellipse class="gang-masks__clown" cx="622" cy="618" rx="150" ry="217" transform="rotate(5 622 618)" fill="url(#clown-mask-tone)"/>
    </g>

    <g class="film-title" aria-label="The Quiet Ledger Affair">
      <text class="title-text" x="0" y="662" font-size="240" textLength="215" lengthAdjust="spacingAndGlyphs" transform="rotate(-7 0 662)">The</text>
      <text class="title-text" x="6" y="872" font-size="240" textLength="300" lengthAdjust="spacingAndGlyphs" transform="rotate(-7 6 872)">Quiet</text>
      <text class="title-text" x="40" y="1070" font-size="240" textLength="780" lengthAdjust="spacingAndGlyphs" transform="rotate(-7 40 1070)">Ledger Affair</text>
    </g>

    <line class="title-underline" x1="38" y1="1132" x2="826" y2="1035" stroke="var(--title-red)" stroke-width="5"/>

    <text class="tagline-text" x="522" y="1114" font-size="32" textLength="285" lengthAdjust="spacingAndGlyphs" transform="rotate(-7 522 1114)">Greed, Betrayal, Murder</text>
  </svg>
</main>
</body>
</html>
```